Stainless Steel Water Bottle Packaging

We need a design for our cylindrical water bottle packaging.

Please see attached template (500ml cola bottle template .ai file) for exact dimensions.

VOLO is defined as the elemental forces of nature embodied in an object or person. The design should be eye catching and draw potential clients in. Although its a cylindrical bottle/box, the front which would face the customer when sitting on a shelf should clearly display our logo.

Requirements
Must have
• Designed to the specifications of the attached template (see attached)
• Our VOLO Logo (see attached) and website www.volobottle.com(in smaller font) must appear.
• Size of bottle must appear - '17 oz/500 ml'
• These should appear somewhere:
• 'INULATED DOUBLE-WALL STAINLESS STEEL WATER BOTTLE'
• 'VOLO Bottles magically keeps drinks cold for up to 24hrs, hot for 12',
• 'BPA Free'
• 'For every VOLO bottle purchased, a portion of proceeds will go towards charity. Each of our colour's have been assigned a specific charity. Please visit www.volobottle.com to find out which charity you helped support!'
• The Top circle - just our Symbol (flame/drop)
• The bottom circle - 'Inc. Designed in Canada made in China' on the outer edge leaving the middle empty for the UPC code.
• Reference website for the bottle case I'm looking for:
• http://shopcorventi.com/t-dune-lagoon-coral-insulated-water-bottle
Nice to have
• illustration of our water bottle shape (see attached) appearing somewhere on the box is something i had in mind but definitely not necessary.

```html
<!DOCTYPE html>
<html lang="en">
<head>
<meta charset="utf-8">
<title>VOLO Bottle Packaging</title>
<link rel="stylesheet" href="https://fonts.googleapis.com/css2?family=Roboto:wght@400;500&family=Roboto+Condensed:wght@400;700&display=swap">
<style>
  :root {
    --page: #f3f2f8;
    --box: #2a2728;
    --cut: #c4262e;
    --blue: #2fa6de;
    --green: #3cbf9b;
    --yellow: #f7c21b;
    --teal: #45c1a6;
    --teal-deep: #2f9f88;
  }
  html, body { margin: 0; padding: 0; overflow: hidden; }
  body { background: var(--page); }
  .canvas {
    position: relative;
    width: 1200px;
    height: 1200px;
    overflow: hidden;
    background: var(--page);
    font-family: "Roboto", Arial, sans-serif;
  }
  .lids { position: absolute; left: 150px; top: 30px; }

  .sleeve {
    position: absolute;
    left: 51px; top: 292px;
    width: 801px; height: 903px;
    background: var(--box);
    outline: 1px solid var(--cut);
  }
  .fold { position: absolute; background: var(--cut); }
  .fold-v { left: 30px; top: 0; width: 1px; height: 100%; }
  .fold-h { left: 30px; right: 0; height: 1px; }

  .brand-block {
    position: absolute;
    left: 200px; top: 70px;
    width: 420px;
    text-align: center;
  }
  .brand-name {
    font-family: "Roboto", Arial, sans-serif;
    font-weight: 500;
    font-size: 72px;
    letter-spacing: 6px;
    line-height: 1;
    color: var(--blue);
    display: inline-flex;
    align-items: center;
    gap: 14px;
  }
  .brand-dot {
    width: 26px; height: 26px;
    border-radius: 50%;
    background: var(--blue);
    display: inline-block;
  }
  .brand-site {
    margin-top: 4px;
    font-size: 19px;
    letter-spacing: 4.6px;
    color: var(--blue);
  }

  .spine-text {
    position: absolute;
    transform-origin: left top;
    transform: rotate(-90deg);
    white-space: nowrap;
  }
  .size-label {
    left: 46px; top: 352px;
    font-size: 23px;
    color: var(--blue);
  }
  .spec-band {
    position: absolute;
    left: 83px; top: 199px;
    width: 46px; height: 659px;
    background: var(--yellow);
  }
  .spec-label {
    left: 92px; top: 853px;
    width: 650px;
    font-family: "Roboto Condensed", Arial, sans-serif;
    font-size: 21px;
    line-height: 28px;
    text-align: center;
    color: var(--box);
  }
  .claim-label {
    left: 133px; top: 855px;
    font-size: 19.5px;
    line-height: 28px;
    color: var(--blue);
  }
  .claim-label strong { font-weight: 500; letter-spacing: 1px; }

  .bottle-outline {
    position: absolute;
    left: 292px; top: 231px;
    width: 197px; height: 625px;
    border-radius: 36px 36px 22px 22px;
    background: linear-gradient(180deg, #2d3b38 0%, #2b3331 100%);
  }
  .bottle-name {
    position: absolute;
    left: 292px; top: 786px;
    width: 197px;
    text-align: center;
    font-weight: 500;
    font-size: 34px;
    letter-spacing: 3px;
    color: var(--blue);
  }

  .bpa {
    position: absolute;
    left: 522px; top: 237px;
    font-size: 30px;
    color: var(--blue);
  }

  .charity {
    position: absolute;
    left: 515px; top: 648px;
    width: 270px;
    margin: 0;
    font-family: "Roboto Condensed", Arial, sans-serif;
    font-size: 15.5px;
    line-height: 23px;
    color: var(--green);
  }
  .charity .inline-brand { color: var(--blue); font-weight: 700; letter-spacing: 1px; }
  .charity strong { font-weight: 700; }

  .product-shot {
    position: absolute;
    left: 939px; top: 428px;
    width: 200px; height: 708px;
    background: linear-gradient(180deg, #9aa39f 0%, #4fc4aa 14%, var(--teal) 60%, var(--teal-deep) 100%);
  }
</style>
</head>
<body>
<div class="canvas">

  <svg class="lids" width="520" height="260" viewBox="150 30 520 260">
    <g class="lid-top">
      <circle cx="276" cy="155" r="121" fill="#2a2728" stroke="#c4262e" stroke-width="1"/>
      <text x="276" y="170" text-anchor="middle" font-family="Roboto, Arial, sans-serif" font-weight="500" font-size="44" letter-spacing="3" fill="#2fa6de">VOLO</text>
    </g>
    <g class="lid-bottom">
      <circle cx="529" cy="155" r="121" fill="#2a2728" stroke="#c4262e" stroke-width="1"/>
      <path id="base-arc" d="M 428.5 172.7 A 102 102 0 0 1 629.5 172.7" fill="none"/>
      <text font-family="Roboto Condensed, Arial, sans-serif" font-size="15.5" fill="#3cbf9b" letter-spacing="0.6">
        <textPath href="#base-arc" startOffset="50%" text-anchor="middle">INC. DESIGNED IN CANADA MADE IN CHINA</textPath>
      </text>
      <circle cx="453" cy="139" r="6.5" fill="none" stroke="#c4262e" stroke-width="1"/>
      <circle cx="616" cy="139" r="6.5" fill="none" stroke="#c4262e" stroke-width="1"/>
    </g>
  </svg>

  <section class="sleeve">
    <div class="fold fold-v"></div>
    <div class="fold fold-h" style="top:30px"></div>
    <div class="fold fold-h" style="top:199px"></div>
    <div class="fold fold-h" style="top:870px"></div>

    <div class="brand-block">
      <div class="brand-name"><span class="brand-dot"></span>VOLO</div>
      <div class="brand-site">www.volobottle.com</div>
    </div>

    <div class="spine-text size-label">17 oz/500 ml</div>
    <div class="spec-band"></div>
    <div class="spine-text spec-label">INULATED DOUBLE-WALL STAINLESS STEEL WATER BOTTLE</div>
    <div class="spine-text claim-label"><strong>VOLO</strong> Bottles magically keeps drinks cold for up to 24hrs, hot for 12</div>

    <div class="bottle-outline" role="img" aria-label="Line illustration of the VOLO water bottle shape in teal outline"></div>
    <div class="bottle-name">VOLO</div>

    <div class="bpa">BPA Free</div>

    <p class="charity">For every <span class="inline-brand">VOLO</span> bottle purchased, a portion of proceeds will go towards charity.<br>Each of our colour's have been assigned a specific charity.<br>Please visit <strong>www.volobottle.com</strong> to find out which charity you helped support!</p>
  </section>

  <div class="product-shot" role="img" aria-label="Photo of the teal VOLO stainless steel bottle with silver cap"></div>

</div>
</body>
</html>
```